Ledgerwise - New design for a couple of our pages

We need a total renovation of one of our webpages. First we would like the "insight and analysis" to be redesigned- for now we think the page is ok, but we want it to be great. We want this design to

We specialize in business intelligence and business management software. We are open for removal of some of the text on the site. Generally, we want the page to reflect that we are a modern technology company. See the frontpage of the website for common colors, however, we are open for better ones. We also need the design implemented on our site. If the page becomes a success, then there is a good chance that we would like a similar design for the other pages as well.Se link for the page that we need improved:https://www.ledgerwise-demo.com/project/innsikt-og-analyse/?lang=en

Our main page also needs to be improved, here you will find our color palette, we would like more modern colors.

Sites we want to see with the new design suggestion:

Main page:
https://www.ledgerwise-demo.com/

about us:
https://www.ledgerwise-demo.com/aboutus/?lang=en

Finance and planning:
https://www.ledgerwise-demo.com/project/finance-and-planning/?lang=en

Retail:
https://www.ledgerwise-demo.com/project/retail/?lang=en

Target Market(s)

30 + / Business oriented / Desicion makers / financial officers / Educated

Industry/Entity Type

Information Technology

Number of Pages Required

5+ page

Font styles to use
Sans Serif

Requirements
Must have
• - Overall, we want the page to trigger the visitor to call us and schedule a meeting.
Nice to have
• Nice to have a sugguestion for a call to action - e.g. contact form. We are open to remove text and add another level of paiges under this one - again, open for suggestions for the content as well.
• We want similar colors to the already used greens and blue shades - but the designer may improble the color selection. Perhaps the designer can suggest a few options.

```html
<!DOCTYPE html>
<html lang="no">
<head>
<meta charset="utf-8">
<title>Innsikt og Analyse – Ledgerwise</title>
<link href="https://fonts.googleapis.com/css2?family=Poppins:wght@300;400;500;600&family=Open+Sans:wght@400;600&display=swap" rel="stylesheet">
<style>
:root{
  --brand:#8e1f62;
  --brand-dark:#6f1450;
  --ink:#222;
  --muted:#777;
  --light:#f4f4f4;
  --line:#e2e2e2;
  --num:#d9d9d9;
  --dark:#2a2d36;
  --footer:#24262d;
  --bar:#1b1c21;
}
*{box-sizing:border-box;margin:0;padding:0}
html,body{width:1200px;height:4198px;overflow:hidden}
body{font-family:"Open Sans",sans-serif;color:var(--ink);font-size:13px;line-height:1.6;background:#fff}
h1,h2,h3,h4{font-family:"Poppins",sans-serif;font-weight:500}
a{color:inherit;text-decoration:none}

/* nav */
.site-nav{height:40px;background:#fff;display:flex;align-items:center;padding:0 175px;position:relative;z-index:2}
.logo{font-family:"Poppins",sans-serif;font-weight:600;font-size:19px;color:var(--muted);display:flex;align-items:center;gap:6px}
.logo i{width:9px;height:9px;background:var(--brand);display:block}
.menu{display:flex;gap:22px;margin-left:70px;font-size:11px;color:#444}
.nav-tools{margin-left:auto;display:flex;gap:14px;align-items:center}
.flag{width:14px;height:9px;background:#b8263a;display:block}

/* hero */
.hero{height:538px;position:relative;text-align:center;color:#fff;
  background:linear-gradient(160deg,#3d3250 0%,#6a2c6b 40%,#b1416f 65%,#2d2e57 100%)}
.hero h1{font-size:46px;font-weight:500;padding-top:190px}
.hero p{font-size:17px;margin-top:2px}
.btn{display:inline-block;background:var(--brand);color:#fff;font-family:"Poppins",sans-serif;font-size:12px;padding:9px 22px}
.hero .btn{background:#fff;color:var(--brand);margin-top:20px;border:2px solid var(--brand)}
.mouse{position:absolute;left:50%;top:448px;margin-left:-12px}

/* competences */
.competences{height:472px;text-align:center;padding-top:80px}
.section-title{font-size:32px;color:var(--ink)}
.lead{color:var(--muted);font-size:11px;margin-top:6px}
.comp-grid{display:grid;grid-template-columns:repeat(6,1fr);row-gap:30px;width:870px;margin:46px auto 0;text-align:left}
.comp .num{font-family:"Poppins",sans-serif;font-size:36px;font-weight:300;color:var(--num);line-height:1}
.comp .label{font-size:12px;color:#333;margin-top:4px;line-height:1.4;padding-right:10px}

/* value */
.value{height:490px;background:var(--light);position:relative}
.value-media{position:absolute;left:175px;top:70px;width:410px;height:350px;
  background:linear-gradient(135deg,#8a8f8b,#c9c4b8 45%,#5f6b6a);}
.play{position:absolute;left:50%;top:50%;width:56px;height:56px;margin:-28px 0 0 -28px;border-radius:50%;background:var(--brand)}
.play:after{content:"";position:absolute;left:22px;top:17px;border-left:16px solid #fff;border-top:11px solid transparent;border-bottom:11px solid transparent}
.value-copy{position:absolute;left:612px;top:88px;width:400px}
.value-copy h2{font-size:34px}
.value-copy p{color:#555;font-size:12px;margin-top:14px}
.value-copy .btn{margin-top:30px}

/* dashboard */
.dashboard{height:718px;text-align:center;padding-top:73px}
.dashboard p{color:#444;font-size:13px;width:720px;margin:16px auto 0}
.dash-media{width:370px;height:322px;margin:48px auto 0;background:linear-gradient(180deg,#e9ebee,#cfd3d8);border-radius:6px}
.caption{font-size:13px;margin-top:22px;color:#333}

/* case */
.case{height:594px;background:var(--light);position:relative;overflow:hidden}
.case-watermark{position:absolute;right:-40px;top:70px;font-family:"Poppins",sans-serif;font-weight:600;font-size:200px;color:#e9e9e9;line-height:1}
.case-head{position:absolute;left:175px;top:60px}
.case-head h2{font-size:34px}
.case-head .view{color:var(--brand);border-bottom:1px solid var(--brand);font-size:13px}
.case-list{position:absolute;left:175px;top:148px;font-size:11px;line-height:1.8}
.case-card{position:absolute;left:332px;top:140px;width:720px;height:400px;background:#fff;box-shadow:0 4px 20px rgba(0,0,0,.06)}
.case-media{position:absolute;left:36px;top:90px;width:285px;height:210px;background:linear-gradient(180deg,#dfe3e8,#b9c0c8);border-radius:5px}
.case-copy{position:absolute;left:358px;top:52px;width:330px}
.case-copy h3{font-size:26px;line-height:1.25}
.case-copy p{font-size:12px;color:#444;margin-top:14px}
.case-copy a{display:inline-block;margin-top:14px;font-weight:600;border-bottom:2px solid var(--ink);font-size:13px}

/* accordion */
.topics{height:403px;background:linear-gradient(120deg,#22252d,#3a3d47 55%,#1f2128);padding-top:62px}
.acc{width:850px;margin:0 auto}
.acc-item{height:44px;background:#fff;margin-bottom:26px;display:flex;align-items:center;justify-content:space-between;padding:0 20px;font-size:13px}
.acc-item b{color:var(--brand);font-size:20px;font-weight:400}

/* related */
.related{height:367px;text-align:center;padding-top:72px}
.services{display:flex;justify-content:center;gap:48px;margin-top:46px}
.svc{width:120px;font-size:13px;font-weight:600}
.svc svg{display:block;margin:0 auto 6px}

/* callback */
.callback{height:431px;background:#f7f7f7;text-align:center;padding-top:38px}
.eyebrow{color:#3a6fd0;font-size:11px}
.callback h2{font-size:32px;margin-top:2px}
.form{width:850px;margin:30px auto 0;text-align:left}
.row{display:flex;gap:40px}
.field{flex:1;border-bottom:1px solid #ccc;height:34px;font-size:11px;color:#888;padding-top:10px}
.field.msg{height:86px;margin-top:26px}
.form .btn{display:block;width:120px;margin:26px auto 0;text-align:center}

/* footer */
.footer{height:95px;background:var(--footer);color:#ddd;display:flex;align-items:center;gap:60px;padding:0 175px}
.fcol{display:flex;gap:10px;align-items:flex-start;font-size:11px;line-height:1.4}
.fcol h4{font-size:13px;color:#fff;font-weight:500}
.social{display:flex;gap:6px;margin-top:4px}
.social i{width:16px;height:16px;background:#5a5d67;display:block}
.bottom-bar{height:50px;background:var(--bar);color:#888;font-size:10px;text-align:center;line-height:50px;position:relative}
.to-top{position:absolute;right:175px;top:0;width:38px;height:38px;background:var(--brand)}
</style>
</head>
<body>

<header class="site-nav">
  <a class="logo" href="https://www.ledgerwise-demo.com/">Ledgerwise<i></i></a>
  <nav class="menu"><a>Hjem</a><a>Bransjer</a><a>Løsninger</a><a>Kurs</a><a>Kunder</a><a>Om oss</a></nav>
  <div class="nav-tools">
    <svg width="12" height="12" viewBox="0 0 12 12"><circle cx="5" cy="5" r="4" fill="none" stroke="#555" stroke-width="1.4"/><line x1="8" y1="8" x2="11" y2="11" stroke="#555" stroke-width="1.4"/></svg>
    <span class="flag"></span>
  </div>
</header>

<section class="hero" role="img" aria-label="Close-up of a laptop keyboard in purple and blue light">
  <h1>Innsikt og Analyse</h1>
  <p>Riktig informasjon. Raskere.</p>
  <a class="btn">Suggestion</a>
  <svg class="mouse" width="24" height="36" viewBox="0 0 24 36"><rect x="2" y="2" width="20" height="32" rx="10" fill="none" stroke="#fff" stroke-width="1.5"/><line x1="12" y1="8" x2="12" y2="14" stroke="#fff" stroke-width="1.5"/></svg>
</section>

<section class="competences">
  <h2 class="section-title">Kjernekompetanse</h2>
  <p class="lead">Vi leverer et bredt spekter av tjenester innen analyse, data og rapportering for moderne virksomheter.</p>
  <div class="comp-grid">
    <div class="comp"><div class="num">01</div><div class="label">Cortex Intelligence</div></div>
    <div class="comp"><div class="num">02</div><div class="label">Advanced Analytics</div></div>
    <div class="comp"><div class="num">03</div><div class="label">Machine Learning</div></div>
    <div class="comp"><div class="num">04</div><div class="label">Internet of Things</div></div>
    <div class="comp"><div class="num">05</div><div class="label">Ledgerwise Flowdesk</div></div>
    <div class="comp"><div class="num">06</div><div class="label">Pulse BI</div></div>
    <div class="comp"><div class="num">07</div><div class="label">Query Server Reporting Services</div></div>
    <div class="comp"><div class="num">08</div><div class="label">Nimbus Data Catalog</div></div>
    <div class="comp"><div class="num">09</div><div class="label">Data Integrasjon</div></div>
    <div class="comp"><div class="num">10</div><div class="label">Nimbus Stream Analytics</div></div>
    <div class="comp"><div class="num">11</div><div class="label">Nimbus Data Lake Analytics</div></div>
  </div>
</section>

<section class="value">
  <div class="value-media" role="img" aria-label="Video still of a presenter showing charts on a projector screen"><span class="play"></span></div>
  <div class="value-copy">
    <h2>Mer verdi av dine data</h2>
    <p>Ledgerwise skaper ny innsikt og gir deg bedre grunnlag for å ta gode beslutninger, raskere og mer presist.</p>
    <p>I Ledgerwise er vi opptatt av å kombinere den beste teknologien med dyp bransjekunnskap og forretningsforståelse.</p>
    <p>Vi er en samarbeidspartner og rådgiver for deg som ønsker mer av egne data.</p>
    <a class="btn">Kontakt oss</a>
  </div>
</section>

<section class="dashboard">
  <h2 class="section-title">Dashbord og Rapportering</h2>
  <p>Få rask og enkel tilgang til nøkkeltall og styringsinformasjon for hele virksomheten, når som helst. Fra én kilde, med oppdaterte tall hver dag.</p>
  <p>Med visuelle dashbord og fleksible rapporter får ledere og medarbeidere et felles bilde av situasjonen, slik at beslutninger tas på riktig grunnlag hver gang.</p>
  <div class="dash-media" role="img" aria-label="Laptop showing a reporting dashboard with tables, bar charts and a pie chart"></div>
  <p class="caption">Reporting has never been better and faster.</p>
</section>

<section class="case">
  <div class="case-watermark">STUDY</div>
  <div class="case-head"><h2>CASE STUDY</h2><a class="view">View all</a></div>
  <div class="case-list">Case A<br>Case B</div>
  <article class="case-card">
    <div class="case-media" role="img" aria-label="Laptop showing a hospital antibiotic usage dashboard"></div>
    <div class="case-copy">
      <h3>Dashboard for antibiotikabruk i sykehus</h3>
      <p>Vi har laget en løsning for sykehusapotekene der de raskt kan følge med på bruken av antibiotika for hver avdeling og hvert sykehus. Data samles automatisk og vises som trender, kart og tabeller slik at fagfolk enkelt ser endringer over tid og kan sette inn tiltak der det trengs.</p>
      <a>Besøk løsningen her</a>
    </div>
  </article>
</section>

<section class="topics" role="region" aria-label="Fagområder">
  <div class="acc">
    <div class="acc-item">Avansert analyse<b>+</b></div>
    <div class="acc-item">Cortex Intelligence Suite<b>+</b></div>
    <div class="acc-item">Pulse BI<b>+</b></div>
    <div class="acc-item">Maskinlæring<b>+</b></div>
  </div>
</section>

<section class="related">
  <h2 class="section-title">Relaterte løsninger og tjenester</h2>
  <div class="services">
    <div class="svc"><svg width="36" height="30" viewBox="0 0 36 30"><path d="M4 10h28l-3 18H7z" fill="var(--brand)"/><path d="M12 10a6 6 0 0 1 12 0" fill="none" stroke="var(--brand)" stroke-width="2"/></svg>Handel</div>
    <div class="svc"><svg width="36" height="30" viewBox="0 0 36 30"><rect x="4" y="4" width="28" height="22" fill="var(--brand)"/><rect x="8" y="8" width="8" height="4" fill="#fff"/></svg>Finans og planlegging</div>
    <div class="svc"><svg width="36" height="30" viewBox="0 0 36 30"><rect x="5" y="16" width="6" height="12" fill="var(--brand)"/><rect x="15" y="8" width="6" height="20" fill="var(--brand)"/><rect x="25" y="2" width="6" height="26" fill="var(--brand)"/></svg>Rapportering</div>
    <div class="svc"><svg width="36" height="30" viewBox="0 0 36 30"><rect x="3" y="3" width="30" height="20" fill="var(--brand)"/><rect x="12" y="25" width="12" height="3" fill="var(--brand)"/></svg>Programvareprodukter</div>
    <div class="svc"><svg width="36" height="30" viewBox="0 0 36 30"><circle cx="12" cy="9" r="6" fill="var(--brand)"/><circle cx="25" cy="11" r="5" fill="var(--brand)"/><path d="M2 28c0-8 20-8 20 0zM18 28c0-6 16-6 16 0z" fill="var(--brand)"/></svg>Rådgivning og tjenester</div>
  </div>
</section>

<section class="callback">
  <p class="eyebrow">Free Consultation</p>
  <h2>Get A Call Back</h2>
  <p class="lead">Legg igjen kontaktinformasjon så ringer vi deg opp for en uforpliktende prat om dine behov.</p>
  <form class="form">
    <div class="row"><div class="field">Name</div><div class="field">Email</div><div class="field">Phone</div></div>
    <div class="field msg">Message</div>
    <a class="btn">SUBMIT</a>
  </form>
</section>

<footer class="footer">
  <div class="fcol"><svg width="16" height="20" viewBox="0 0 16 20"><path d="M8 1a6 6 0 0 1 6 6c0 5-6 12-6 12S2 12 2 7a6 6 0 0 1 6-6z" fill="#fff"/><circle cx="8" cy="7" r="2" fill="var(--footer)"/></svg><div><h4>Office</h4>Havnegata 14, 7010 Trondheim</div></div>
  <div class="fcol"><svg width="18" height="18" viewBox="0 0 18 18"><path d="M4 1l3 4-2 2a10 10 0 0 0 6 6l2-2 4 3-2 3C8 17 1 10 1 3z" fill="#fff"/></svg><div><h4>Call us</h4>+47 40 12 34 56</div></div>
  <div class="fcol"><svg width="18" height="14" viewBox="0 0 18 14"><rect x="1" y="1" width="16" height="12" fill="none" stroke="#fff" stroke-width="1.5"/><path d="M1 1l8 7 8-7" fill="none" stroke="#fff" stroke-width="1.5"/></svg><div><h4>Email</h4>kontakt@ledgerwise-demo.com</div></div>
  <div class="fcol"><div><h4>Get social</h4><div class="social"><i></i><i></i><i></i><i></i></div></div></div>
</footer>
<div class="bottom-bar">Copyright © 2019 Ledgerwise AS | All rights reserved<span class="to-top"></span></div>

</body>
</html>
```